Medida Certa - Working hours register App needs interface design

Medida Certa, a 1 million users Brazilian website focused on general calculations needs an interface to an App for registering the working hours of a housemaid, a nanny, a housekeeper or other domestic workers.
The final users should be mainly housewifes.
The wireframe of the pages is in the LarPonto_layout.xls file attached.
Logo is also available in the wireframe.
The interface should be optimized for Android on Orbita KX with a 5'' screen.
Target Market(s)
Females, educated, from 30 to 50 y.o.
Industry/Entity Type
Android
Look and feel
Each slider illustrates characteristics of the customer's brand and the style your logo design should communicate.

```html
<!DOCTYPE html>
<html lang="en">
<head>
<meta charset="utf-8">
<title>Menu</title>
<link rel="stylesheet" href="https://fonts.googleapis.com/css2?family=Barlow:wght@600;700&display=swap">
<style>
  :root {
    --brand-red: #c30000;
    --field-grey: #e9e9e9;
    --accent-pink: #e8336e;
    --button-top: #ff5c8c;
    --button-bottom: #f2406f;
    --button-edge: #b8103f;
    --ink: #1e1e1e;
    --white: #ffffff;
  }
  * { box-sizing: border-box; margin: 0; padding: 0; }
  html, body { width: 720px; height: 1200px; overflow: hidden; background: var(--white); }
  body { position: relative; font-family: "Barlow", "Arial Narrow", sans-serif; }

  .app-header {
    position: absolute; left: 0; top: 0; width: 720px; height: 99px;
    background: var(--brand-red); color: var(--white);
    display: flex; align-items: center; justify-content: center;
    font-size: 47px; font-weight: 700; letter-spacing: 0.5px;
  }
  .app-footer {
    position: absolute; left: 0; top: 1176px; width: 720px; height: 24px;
    background: var(--brand-red);
  }

  .worker { position: absolute; left: 15px; width: 690px; height: 162px; }
  .worker-photo {
    position: absolute; left: 0; top: 0; width: 95px; height: 95px;
    background: linear-gradient(135deg, #5a6b3c, #c99a80);
  }
  .worker-photo.light { background: linear-gradient(135deg, #cfd3cc, #8a7a70); }
  .worker-photo.warm { background: linear-gradient(135deg, #3f5a4a, #b07a5e); }
  .worker-name {
    position: absolute; left: 102px; top: 0; width: 586px; height: 95px;
    background: var(--field-grey); border-bottom: 3px solid var(--accent-pink);
    display: flex; align-items: center; padding-left: 9px;
    font-size: 36px; font-weight: 700; color: var(--ink);
  }
  .worker-name.indented { padding-left: 17px; }
  .worker-actions { position: absolute; top: 108px; left: 258px; display: flex; gap: 14px; }
  .action-button {
    width: 208px; height: 53px;
    background: linear-gradient(var(--button-top), var(--button-bottom));
    border-bottom: 3px solid var(--button-edge);
    color: var(--white); font-size: 26px; font-weight: 700;
    display: flex; align-items: center; justify-content: center; gap: 10px;
  }
  .action-button svg { fill: var(--white); }
</style>
</head>
<body>
  <header class="app-header">Menu</header>

  <section class="worker" style="top:114px">
    <div class="worker-photo warm" role="img" aria-label="Portrait photo of the worker"></div>
    <div class="worker-name">Marina Albuquerquena</div>
    <div class="worker-actions">
      <div class="action-button"><svg width="24" height="30" viewBox="0 0 24 30"><path d="M17 1l6 4-13 20-7 4 1-8z"/></svg>Edit</div>
      <div class="action-button"><svg width="34" height="22" viewBox="0 0 34 22"><path d="M0 0h34v22H0z M3 3v4h4V3z M9 3v4h4V3z M15 3v4h4V3z M21 3v4h4V3z M27 3v4h4V3z M3 9v4h4V9z M9 9v4h4V9z M15 9v4h4V9z M21 9v4h4V9z M27 9v4h4V9z M7 15v4h20v-4z" fill-rule="evenodd"/></svg>Enter Data</div>
    </div>
  </section>

  <section class="worker" style="top:369px">
    <div class="worker-photo" role="img" aria-label="Portrait photo of the worker"></div>
    <div class="worker-name indented">Renata</div>
    <div class="worker-actions">
      <div class="action-button"><svg width="24" height="30" viewBox="0 0 24 30"><path d="M17 1l6 4-13 20-7 4 1-8z"/></svg>Edit</div>
      <div class="action-button"><svg width="34" height="22" viewBox="0 0 34 22"><path d="M0 0h34v22H0z M3 3v4h4V3z M9 3v4h4V3z M15 3v4h4V3z M21 3v4h4V3z M27 3v4h4V3z M3 9v4h4V9z M9 9v4h4V9z M15 9v4h4V9z M21 9v4h4V9z M27 9v4h4V9z M7 15v4h20v-4z" fill-rule="evenodd"/></svg>Enter Data</div>
    </div>
  </section>

  <section class="worker" style="top:606px">
    <div class="worker-photo light" role="img" aria-label="Portrait photo of the worker"></div>
    <div class="worker-name">Clara Moura</div>
    <div class="worker-actions">
      <div class="action-button"><svg width="24" height="30" viewBox="0 0 24 30"><path d="M17 1l6 4-13 20-7 4 1-8z"/></svg>Edit</div>
      <div class="action-button"><svg width="34" height="22" viewBox="0 0 34 22"><path d="M0 0h34v22H0z M3 3v4h4V3z M9 3v4h4V3z M15 3v4h4V3z M21 3v4h4V3z M27 3v4h4V3z M3 9v4h4V9z M9 9v4h4V9z M15 9v4h4V9z M21 9v4h4V9z M27 9v4h4V9z M7 15v4h20v-4z" fill-rule="evenodd"/></svg>Enter Data</div>
    </div>
  </section>

  <section class="worker" style="top:847px">
    <div class="worker-photo warm" role="img" aria-label="Portrait photo of the worker"></div>
    <div class="worker-name">Marina Albuquerquena</div>
    <div class="worker-actions">
      <div class="action-button"><svg width="24" height="30" viewBox="0 0 24 30"><path d="M17 1l6 4-13 20-7 4 1-8z"/></svg>Edit</div>
      <div class="action-button"><svg width="34" height="22" viewBox="0 0 34 22"><path d="M0 0h34v22H0z M3 3v4h4V3z M9 3v4h4V3z M15 3v4h4V3z M21 3v4h4V3z M27 3v4h4V3z M3 9v4h4V9z M9 9v4h4V9z M15 9v4h4V9z M21 9v4h4V9z M27 9v4h4V9z M7 15v4h20v-4z" fill-rule="evenodd"/></svg>Enter Data</div>
    </div>
  </section>

  <footer class="app-footer"></footer>
</body>
</html>
```